Redesign My Travel Voucher Coupons-Please redesign the flyers I have attached to this brief.

These designs will be catered towards like travel agency vacation stays...luxury resort stays, hotel and airfare getaways, etc. so must have a travel theme but more importantly professional trustworthy appeal...

Please redesign the flyers I have attached to this brief.

I have attached my existing designs. Please use all existing content and elements exactly but make the design much better...also, please keep in mind that these would be full color and printer friendly...

Target Market(s)

Consumers. People receive these vouchers from businesses that run marketing promotions and contests and giveaways. So the look and feel must feel professional and trustworthy but not cheesy and fake.

Industry/Entity Type

Hotel

Requirements
Must have
• Please use all existing content and elements exactly but make the design much better...also, please keep in mind that these would be full color and printer friendly...

MUST HAVE ALL EXISTING CONTENT EXACT NO EXCEPTIONS
Nice to have
• These designs will be catered towards like travel agency vacation stays...luxury resort stays, hotel and airfare getaways, etc. so must have a travel theme but more importantly professional trustworthy appeal...

Should not have

```html
<!DOCTYPE html>
<html lang="en">
<head>
<meta charset="utf-8">
<title>Travel Voucher Flyers</title>
<link rel="stylesheet" href="https://fonts.googleapis.com/css2?family=Anton&family=Montserrat:wght@400;500;600;700;800&display=swap">
<style>
:root{
  --board:#a5e3e0;
  --orange:#f26522;
  --amber:#f7a21b;
  --teal:#2ab7b1;
  --teal-soft:#a9e4df;
  --cream:#fdf0e0;
  --ink:#3a3a3a;
  --ink-dark:#2a2a2a;
  --brown:#5a3419;
  --muted:#7b7b7b;
  --brand:#2c6fb7;
}
*{box-sizing:border-box;margin:0;padding:0}
html,body{width:1200px;height:1036px;overflow:hidden}
body{background:var(--board);position:relative;font-family:"Montserrat",sans-serif;color:var(--ink)}

.flyer{position:absolute;width:1063px;height:1504px;background:#fff;transform-origin:0 0;overflow:hidden;box-shadow:0 6px 18px rgba(0,0,0,.18)}
.flyer--main{left:38px;top:52px;transform:scale(.6)}
.flyer--thumb{transform:scale(.1873)}
.thumb-1{left:726px;top:54px}.thumb-2{left:961px;top:54px}
.thumb-3{left:726px;top:366px}.thumb-4{left:961px;top:366px}
.thumb-5{left:726px;top:678px}.thumb-6{left:961px;top:678px}

.hero{position:absolute;left:0;top:0;width:1063px;height:470px}
.sponsor{position:absolute;left:780px;top:28px;width:270px;text-align:center}
.sponsor__label{font-size:19px;font-weight:500;color:var(--brown)}
.sponsor__brand{display:flex;align-items:center;justify-content:center;gap:7px;margin:14px 0 16px;font-size:16px;font-weight:700;color:var(--brand)}
.sponsor__brand i{width:14px;height:14px;background:var(--brand);display:block}
.sponsor__name,.sponsor__phone{font-size:14px;color:var(--muted);font-weight:500;line-height:22px}

.headline{position:absolute;left:30px;top:78px;display:flex;align-items:flex-start}
.headline__main{background:var(--orange);color:#fff;font-family:"Anton",sans-serif;font-size:64px;line-height:80px;padding:0 62px 0 28px;clip-path:polygon(10% 0,100% 0,96% 100%,0 100%);letter-spacing:1px}
.headline__tag{margin-left:-12px;margin-top:6px;background:var(--amber);color:#fff;font-family:"Anton",sans-serif;padding:6px 16px 4px 22px;clip-path:polygon(4% 0,100% 0,98% 100%,0 100%)}
.headline__tag small{display:block;font-size:19px;color:#fde6a8;line-height:22px}
.headline__tag span{display:block;font-size:29px;line-height:34px}
.subtitle{position:absolute;left:40px;top:156px;width:342px;background:rgba(42,183,177,.92);color:#fff;font-size:18px;font-weight:500;line-height:24px;padding:10px 20px 12px}

.photo{position:absolute;border:5px solid var(--teal-soft);border-radius:16px}
.photo--beach{left:768px;top:375px;width:256px;height:256px;background:linear-gradient(160deg,#9fd2ee 0%,#e8e1d0 45%,#48b7c7 70%,#2c8fa9 100%)}
.photo--lounger{left:812px;top:646px;width:212px;height:212px;background:linear-gradient(150deg,#eef2ec 0%,#c9b79a 45%,#7a6a57 75%,#3d3a34 100%)}
.photo--pool{left:820px;top:890px;width:200px;height:200px;background:linear-gradient(180deg,#1a1610 0%,#c78a2e 40%,#3b2a18 58%,#1ea7e6 80%,#0d6fbf 100%)}

.banner{position:absolute;color:#fff;font-family:"Anton",sans-serif;font-size:25px;line-height:48px;padding-left:18px;clip-path:polygon(0 4%,100% 0,84% 100%,3% 100%)}
.banner--orange{background:var(--orange)}
.banner--teal{background:var(--teal)}
.banner--exclusive{left:55px;top:478px;width:296px}
.banner--features{left:55px;top:674px;width:296px}
.banner--how{left:55px;top:872px;width:374px}
.banner--say{left:70px;top:1108px;width:372px}

.copy{position:absolute;font-size:15.3px;line-height:19.4px;color:var(--ink)}
.copy--exclusive{left:67px;top:542px;width:680px}
.copy--how{left:73px;top:934px;width:730px}

.features{position:absolute;left:40px;top:700px;width:754px;height:148px;background:var(--cream);border-radius:16px;padding:38px 0 0 32px;display:grid;grid-template-columns:328px 1fr;row-gap:7px}
.features li{list-style:none;font-size:13.6px;font-weight:500;display:flex;align-items:center;gap:6px;color:var(--ink)}
.features svg{width:16px;height:16px;flex:none}

.testimonial{position:absolute;left:70px;top:1132px;width:948px;height:150px;background:var(--teal-soft);border-radius:22px;padding:44px 34px 0 34px;font-size:15px;line-height:19.5px;color:var(--ink-dark)}
.testimonial cite{display:block;font-style:normal;font-weight:700}

.cutline{position:absolute;left:0;top:1314px;width:1063px;border-top:2px dashed #888}
.scissors{position:absolute;left:26px;top:1298px;width:48px;height:30px}
.divider{position:absolute;left:280px;top:1326px;height:178px;border-left:2px dashed #888}
.cert{position:absolute;left:20px;top:1350px;width:262px;text-align:center;font-weight:800}
.cert__label{font-size:21px;color:var(--ink-dark);line-height:30px}
.cert__value{font-size:26px;color:var(--orange);line-height:30px}
.redeem{position:absolute;left:334px;top:1350px;width:720px}
.redeem__title{font-size:23px;font-weight:800;color:var(--ink-dark);line-height:31px}
.redeem__url{font-size:35px;font-weight:800;color:var(--orange);line-height:42px;margin-top:4px;letter-spacing:.3px}
.redeem__note{font-size:16px;color:var(--ink)}
</style>
</head>
<body>

<svg width="0" height="0" style="position:absolute">
  <defs>
    <symbol id="tick" viewBox="0 0 16 16"><circle cx="8" cy="8.5" r="6.5" fill="none" stroke="#f26522" stroke-width="1.4"/><path d="M4.5 8.5l2.6 2.6L14 3" fill="none" stroke="#f26522" stroke-width="1.8" stroke-linecap="round"/></symbol>
  </defs>
</svg>

<!-- Main voucher -->
<article class="flyer flyer--main">
  <svg class="hero" viewBox="0 0 1063 470" role="img" aria-label="Photo of a pink luxury resort tower above a tropical marina and palm trees">
    <defs>
      <linearGradient id="heroMain" x1="0" y1="0" x2="0" y2="1">
        <stop offset="0" stop-color="#2b8fd6"/><stop offset=".35" stop-color="#6fb8e8"/>
        <stop offset=".5" stop-color="#d99b86"/><stop offset=".7" stop-color="#4c7a3f"/><stop offset="1" stop-color="#2e9fb0"/>
      </linearGradient>
    </defs>
    <rect width="1063" height="470" fill="url(#heroMain)"/>
    <path d="M735 0C760 120 860 190 1063 200V0Z" fill="#fff"/>
    <path d="M0 438C220 380 420 470 640 425S930 370 1063 392V470H0Z" fill="#fff"/>
  </svg>
  <div class="sponsor">
    <p class="sponsor__label">Compliments Of</p>
    <p class="sponsor__brand"><i></i>Northwind Rewards</p>
    <p class="sponsor__name">Dana Ellis</p>
    <p class="sponsor__phone">555-014-2290</p>
  </div>
  <div class="headline">
    <h1 class="headline__main">ENJOY</h1>
    <p class="headline__tag"><small>7 NIGHTS</small><span>IN A LUXURY RESORT</span></p>
  </div>
  <p class="subtitle">7 Nights Luxury Resort Getaway<br>Over 3500 Locations Worldwide<br>To Choose From</p>

  <div class="photo photo--beach" role="img" aria-label="Aerial photo of a beachfront hotel strip"></div>
  <div class="photo photo--lounger" role="img" aria-label="Photo of a guest in a straw hat on a pool lounger"></div>
  <div class="photo photo--pool" role="img" aria-label="Photo of a resort pool lit up at night"></div>

  <h2 class="banner banner--orange banner--exclusive">EXCLUSIVELY FOR:</h2>
  <p class="copy copy--exclusive">Congratulations, you are the recipient of 7 nights luxury resort accommodations. This special offer is good for two adults. Two adults 7 nights of luxurious resort accommodations in one of 3500 available resorts worldwide. Choose from<br>thousands of U.S destinations and hundreds of International destinations. Lots of local drive-to resorts as well as exotic fly-to destinations.</p>

  <ul class="features">
    <li><svg><use href="#tick"/></svg>Travel 7 Days A Week</li>
    <li><svg><use href="#tick"/></svg>Your Choice Of Over 50 Luxury Destinations</li>
    <li><svg><use href="#tick"/></svg>Good For Two Adults &amp; Two Children</li>
    <li><svg><use href="#tick"/></svg>Pay Just The Taxes &amp; Fees</li>
    <li><svg><use href="#tick"/></svg>Multiple Travel Date Requests Allowed</li>
    <li><svg><use href="#tick"/></svg>Fully Transferable To Another Person</li>
    <li><svg><use href="#tick"/></svg>No Timeshare No Sales Presentation Guaranteed!</li>
    <li><svg><use href="#tick"/></svg>24 Months To Complete Travel After Redemption</li>
  </ul>
  <h2 class="banner banner--teal banner--features">FEATURES</h2>

  <h2 class="banner banner--orange banner--how">HOW CAN WE DO THIS?</h2>
  <p class="copy copy--how">We contract with the world leading hotel chains and resorts to help them fill their otherwise empty rooms. We help fill empty rooms which the hotels, resorts and cruise lines turn into additional revenue from other areas of their property and future bookings. Hotels rarely experience full occupancy, yet they remain open, providing rooms and services at fixed costs. So when hotels give out their rooms by partnering with marketing companies like us, they might miss out on the room fee, but they already didn't have that in the first place, at least now they have the opportunity to gain a customer for their in-house restaurants, room service, their casinos, an extra day stay, future bookings, etc.</p>

  <blockquote class="testimonial">"We won this trip at a raffle at this annual golf show and was able to use it for our honeymoon! We were able to go right away after our wedding. The resort was amazing. The pools, the beach, the whole deal. The real deal. Thank you!"<cite>Leo M. Atlanta, Georgia</cite></blockquote>
  <h2 class="banner banner--orange banner--say">WHAT OTHERS SAY</h2>

  <div class="cutline"></div>
  <svg class="scissors" viewBox="0 0 48 30"><circle cx="8" cy="8" r="5" fill="none" stroke="#777" stroke-width="2"/><circle cx="8" cy="22" r="5" fill="none" stroke="#777" stroke-width="2"/><path d="M12 11L46 20M12 19L46 10" stroke="#777" stroke-width="2"/></svg>
  <div class="divider"></div>
  <div class="cert">
    <p class="cert__label">Certificate ID</p>
    <p class="cert__value">107083-11266</p>
    <p class="cert__label">Expires</p>
    <p class="cert__value">11/11/2020</p>
  </div>
  <div class="redeem">
    <p class="redeem__title">VIEW ALL THE DETAILS OF THIS SPECIAL OFFER<br>AND REDEEM ONLINE AT</p>
    <p class="redeem__url">WWW.GETAWAYREWARDSHUB.COM</p>
    <p class="redeem__note">*Terms and Conditions apply see website for details</p>
  </div>
</article>

<!-- Variant vouchers -->
<article class="flyer flyer--thumb thumb-1">
  <div class="hero" role="img" aria-label="Photo of friends toasting at a restaurant table" style="background:linear-gradient(180deg,#3a1f14,#9a5a36 60%,#d9a276)"></div>
  <div class="sponsor"><p class="sponsor__label">Compliments Of</p><p class="sponsor__brand"><i></i>Northwind Rewards</p><p class="sponsor__name">Dana Ellis</p><p class="sponsor__phone">555-014-2290</p></div>
  <div class="headline"><h1 class="headline__main">ENJOY</h1><p class="headline__tag"><span>$ 500 OFF</span></p></div>
  <p class="subtitle">$ 500 Off At Thousands Of<br>Participating Restaurant</p>
  <div class="photo photo--beach" role="img" aria-label="Photo of diners at a table" style="background:linear-gradient(160deg,#5a4030,#c9a27e)"></div>
  <div class="photo photo--lounger" role="img" aria-label="Photo of a plated sushi dish" style="background:linear-gradient(160deg,#3a2a22,#d35a3a)"></div>
  <div class="photo photo--pool" role="img" aria-label="Photo of a gourmet plate" style="background:linear-gradient(160deg,#6b4a30,#e0b080)"></div>
  <h2 class="banner banner--orange banner--exclusive">EXCLUSIVELY FOR:</h2>
  <p class="copy copy--exclusive">Congratulations, you are the recipient of a special dining offer for two adults. Enjoy savings at thousands of participating restaurants across the country, from local favorites to fine dining spots in many cities.</p>
  <ul class="features"><li><svg><use href="#tick"/></svg>Dine 7 Days A Week</li><li><svg><use href="#tick"/></svg>Choose Many Restaurants</li><li><svg><use href="#tick"/></svg>Good For Two Adults</li><li><svg><use href="#tick"/></svg>Pay Just The Taxes</li><li><svg><use href="#tick"/></svg>Flexible Dates Allowed</li><li><svg><use href="#tick"/></svg>Fully Transferable</li><li><svg><use href="#tick"/></svg>No Sales Pitch</li><li><svg><use href="#tick"/></svg>24 Months To Redeem</li></ul>
  <h2 class="banner banner--teal banner--features">FEATURES</h2>
  <h2 class="banner banner--orange banner--how">HOW CAN WE DO THIS?</h2>
  <p class="copy copy--how">We partner with leading restaurant groups to help them fill open tables. Empty seats cost money, so venues gain a new loyal guest while you enjoy a great meal at a lower price, again and again.</p>
  <blockquote class="testimonial">"We used this for our anniversary dinner and it was wonderful. Great food, great service. Thank you!"<cite>Leo M. Atlanta, Georgia</cite></blockquote>
  <h2 class="banner banner--orange banner--say">WHAT OTHERS SAY</h2>
  <div class="cutline"></div><div class="divider"></div>
  <div class="cert"><p class="cert__label">Certificate ID</p><p class="cert__value">107083-11266</p><p class="cert__label">Expires</p><p class="cert__value">11/11/2020</p></div>
  <div class="redeem"><p class="redeem__title">VIEW ALL THE DETAILS OF THIS SPECIAL OFFER<br>AND REDEEM ONLINE AT</p><p class="redeem__url">WWW.GETAWAYREWARDSHUB.COM</p><p class="redeem__note">*Terms and Conditions apply see website for details</p></div>
</article>

<article class="flyer flyer--thumb thumb-2">
  <div class="hero" role="img" aria-label="Photo of a traveller watching a plane at an airport window" style="background:linear-gradient(180deg,#cfd6da,#7a8a96 55%,#2f3a44)"></div>
  <div class="sponsor"><p class="sponsor__label">Compliments Of</p><p class="sponsor__brand"><i></i>Northwind Rewards</p><p class="sponsor__name">Dana Ellis</p><p class="sponsor__phone">555-014-2290</p></div>
  <div class="headline"><h1 class="headline__main">ENJOY</h1><p class="headline__tag"><span>$500 OFF</span></p></div>
  <p class="subtitle">Get $500 Off At Off Over 400,000<br>Hotel &amp; Resort Properties<br>Worldwide</p>
  <div class="photo photo--beach" role="img" aria-label="Photo of a drink by the sea" style="background:linear-gradient(160deg,#f2e6d6,#c8a37a)"></div>
  <div class="photo photo--lounger" role="img" aria-label="Photo of a toy piggy bank in sunglasses" style="background:linear-gradient(160deg,#f3d5d5,#e05a5a)"></div>
  <div class="photo photo--pool" role="img" aria-label="Photo of a piggy bank in a pool float" style="background:linear-gradient(160deg,#8ad8f0,#f4a6c4)"></div>
  <h2 class="banner banner--orange banner--exclusive">EXCLUSIVELY FOR:</h2>
  <p class="copy copy--exclusive">Congratulations, you are the recipient of a hotel savings offer good for two adults. Apply it to stays at thousands of hotels and resorts in U.S and international cities worldwide.</p>
  <ul class="features"><li><svg><use href="#tick"/></svg>Travel 7 Days A Week</li><li><svg><use href="#tick"/></svg>Many Destinations</li><li><svg><use href="#tick"/></svg>Good For Two Adults</li><li><svg><use href="#tick"/></svg>Pay Just The Taxes</li><li><svg><use href="#tick"/></svg>Flexible Dates Allowed</li><li><svg><use href="#tick"/></svg>Fully Transferable</li><li><svg><use href="#tick"/></svg>No Sales Pitch</li><li><svg><use href="#tick"/></svg>24 Months To Travel</li></ul>
  <h2 class="banner banner--teal banner--features">FEATURES</h2>
  <h2 class="banner banner--orange banner--how">HOW CAN WE DO THIS?</h2>
  <p class="copy copy--how">We contract with leading hotel chains to help fill their empty rooms. Hotels gain new guests for dining, spa and future stays, while you enjoy a great getaway at a reduced rate, again and again.</p>
  <blockquote class="testimonial">"We won this trip at a raffle and used it for our honeymoon. The hotel was amazing. Thank you!"<cite>Leo M. Atlanta, Georgia</cite></blockquote>
  <h2 class="banner banner--orange banner--say">WHAT OTHERS SAY</h2>
  <div class="cutline"></div><div class="divider"></div>
  <div class="cert"><p class="cert__label">Certificate ID</p><p class="cert__value">107083-11266</p><p class="cert__label">Expires</p><p class="cert__value">11/11/2020</p></div>
  <div class="redeem"><p class="redeem__title">VIEW ALL THE DETAILS OF THIS SPECIAL OFFER<br>AND REDEEM ONLINE AT</p><p class="redeem__url">WWW.GETAWAYREWARDSHUB.COM</p><p class="redeem__note">*Terms and Conditions apply see website for details</p></div>
</article>

<article class="flyer flyer--thumb thumb-3">
  <div class="hero" role="img" aria-label="Photo of a Mexican beach resort with blue cabanas" style="background:linear-gradient(180deg,#3d8fd6,#8fc8ea 40%,#2a6fb0 60%,#5a8a3a)"></div>
  <div class="sponsor"><p class="sponsor__label">Compliments Of</p><p class="sponsor__brand"><i></i>Northwind Rewards</p><p class="sponsor__name">Dana Ellis</p><p class="sponsor__phone">555-014-2290</p></div>
  <div class="headline"><h1 class="headline__main">ENJOY</h1><p class="headline__tag"><small>MEXICO RESORT</small><span>LUXURY</span></p></div>
  <p class="subtitle">4 Nights Mexico Beach<br>Resort Getaway</p>
  <div class="photo photo--beach" role="img" aria-label="Photo of a resort pool" style="background:linear-gradient(160deg,#8fd0f0,#35b0c8)"></div>
  <div class="photo photo--lounger" role="img" aria-label="Photo of a rock arch at sea" style="background:linear-gradient(160deg,#6fc0e0,#2a7a9a)"></div>
  <div class="photo photo--pool" role="img" aria-label="Photo of palm trees on a beach" style="background:linear-gradient(160deg,#2a8fd0,#e0d8b0)"></div>
  <h2 class="banner banner--orange banner--exclusive">EXCLUSIVELY FOR:</h2>
  <p class="copy copy--exclusive">Congratulations, you are the recipient of 4 nights beach resort accommodations for two adults. Choose from many oceanfront resorts along the Mexican coast with pools and beaches.</p>
  <ul class="features"><li><svg><use href="#tick"/></svg>Travel 7 Days A Week</li><li><svg><use href="#tick"/></svg>Many Beach Resorts</li><li><svg><use href="#tick"/></svg>Good For Two Adults</li><li><svg><use href="#tick"/></svg>Pay Just The Taxes</li><li><svg><use href="#tick"/></svg>Flexible Dates Allowed</li><li><svg><use href="#tick"/></svg>Fully Transferable</li><li><svg><use href="#tick"/></svg>No Sales Pitch</li><li><svg><use href="#tick"/></svg>24 Months To Travel</li></ul>
  <h2 class="banner banner--teal banner--features">FEATURES</h2>
  <h2 class="banner banner--orange banner--how">HOW CAN WE DO THIS?</h2>
  <p class="copy copy--how">We contract with leading resorts to help them fill empty rooms. Resorts earn from dining, activities and future bookings, while you enjoy a beach getaway at a fraction of the usual cost.</p>
  <blockquote class="testimonial">"The resort was amazing. The pools, the beach, the whole deal. The real deal. Thank you!"<cite>Leo M. Atlanta, Georgia</cite></blockquote>
  <h2 class="banner banner--orange banner--say">WHAT OTHERS SAY</h2>
  <div class="cutline"></div><div class="divider"></div>
  <div class="cert"><p class="cert__label">Certificate ID</p><p class="cert__value">107083-11266</p><p class="cert__label">Expires</p><p class="cert__value">11/11/2020</p></div>
  <div class="redeem"><p class="redeem__title">VIEW ALL THE DETAILS OF THIS SPECIAL OFFER<br>AND REDEEM ONLINE AT</p><p class="redeem__url">WWW.GETAWAYREWARDSHUB.COM</p><p class="redeem__note">*Terms and Conditions apply see website for details</p></div>
</article>

<article class="flyer flyer--thumb thumb-4">
  <div class="hero" role="img" aria-label="Photo of a cruise ship docked beside a beach" style="background:linear-gradient(180deg,#4f9ee0,#cfe3f0 45%,#2a6fb0 65%,#d8cfa8)"></div>
  <div class="sponsor"><p class="sponsor__label">Compliments Of</p><p class="sponsor__brand"><i></i>Northwind Rewards</p><p class="sponsor__name">Dana Ellis</p><p class="sponsor__phone">555-014-2290</p></div>
  <div class="headline"><h1 class="headline__main">ENJOY</h1><p class="headline__tag"><small>4 NIGHT</small><span>LUXURY CRUISE</span></p></div>
  <p class="subtitle">A 4 Night Luxury Cruise Getaway</p>
  <div class="photo photo--beach" role="img" aria-label="Photo of a colourful harbour house" style="background:linear-gradient(160deg,#7ac8e8,#e07a4a)"></div>
  <div class="photo photo--lounger" role="img" aria-label="Photo of a coastal town" style="background:linear-gradient(160deg,#f0c080,#3a9ac0)"></div>
  <div class="photo photo--pool" role="img" aria-label="Photo of palms on a beach" style="background:linear-gradient(160deg,#4aa0d8,#f0e6c8)"></div>
  <h2 class="banner banner--orange banner--exclusive">EXCLUSIVELY FOR:</h2>
  <p class="copy copy--exclusive">Congratulations, you are the recipient of a 4 night cruise for two adults. Sail to sunny ports of call with dining, shows and onboard fun included in your stay.</p>
  <ul class="features"><li><svg><use href="#tick"/></svg>Sail Many Weeks</li><li><svg><use href="#tick"/></svg>Choice Of Routes</li><li><svg><use href="#tick"/></svg>Good For Two Adults</li><li><svg><use href="#tick"/></svg>Pay Just The Taxes</li><li><svg><use href="#tick"/></svg>Flexible Dates Allowed</li><li><svg><use href="#tick"/></svg>Fully Transferable</li><li><svg><use href="#tick"/></svg>No Sales Pitch</li><li><svg><use href="#tick"/></svg>24 Months To Travel</li></ul>
  <h2 class="banner banner--teal banner--features">FEATURES</h2>
  <h2 class="banner banner--orange banner--how">HOW CAN WE DO THIS?</h2>
  <p class="copy copy--how">We work with cruise lines to fill open cabins. Ships earn from dining, excursions and future sailings, while you enjoy a relaxing cruise for just the taxes and port fees.</p>
  <blockquote class="testimonial">"We went right after our wedding. The ship, the food, the whole deal. Thank you!"<cite>Leo M. Atlanta, Georgia</cite></blockquote>
  <h2 class="banner banner--orange banner--say">WHAT OTHERS SAY</h2>
  <div class="cutline"></div><div class="divider"></div>
  <div class="cert"><p class="cert__label">Certificate ID</p><p class="cert__value">107083-11266</p><p class="cert__label">Expires</p><p class="cert__value">11/11/2020</p></div>
  <div class="redeem"><p class="redeem__title">VIEW ALL THE DETAILS OF THIS SPECIAL OFFER<br>AND REDEEM ONLINE AT</p><p class="redeem__url">WWW.GETAWAYREWARDSHUB.COM</p><p class="redeem__note">*Terms and Conditions apply see website for details</p></div>
</article>

<article class="flyer flyer--thumb thumb-5">
  <div class="hero" role="img" aria-label="Photo of a traveller watching a plane at an airport window" style="background:linear-gradient(180deg,#cfd6da,#7a8a96 55%,#2f3a44)"></div>
  <div class="sponsor"><p class="sponsor__label">Compliments Of</p><p class="sponsor__brand"><i></i>Northwind Rewards</p><p class="sponsor__name">Dana Ellis</p><p class="sponsor__phone">555-014-2290</p></div>
  <div class="headline"><h1 class="headline__main">ENJOY</h1><p class="headline__tag"><span>$500 OFF</span></p></div>
  <p class="subtitle">Get $500 Off At Off Over 400,000<br>Hotel &amp; Resort Properties<br>Worldwide</p>
  <div class="photo photo--beach" role="img" aria-label="Photo of a drink by the sea" style="background:linear-gradient(160deg,#f2e6d6,#c8a37a)"></div>
  <div class="photo photo--lounger" role="img" aria-label="Photo of a toy piggy bank in sunglasses" style="background:linear-gradient(160deg,#f3d5d5,#e05a5a)"></div>
  <div class="photo photo--pool" role="img" aria-label="Photo of a piggy bank in a pool float" style="background:linear-gradient(160deg,#8ad8f0,#f4a6c4)"></div>
  <h2 class="banner banner--orange banner--exclusive">EXCLUSIVELY FOR:</h2>
  <p class="copy copy--exclusive">Congratulations, you are the recipient of a hotel savings offer good for two adults. Apply it to stays at thousands of hotels and resorts in U.S and international cities worldwide.</p>
  <ul class="features"><li><svg><use href="#tick"/></svg>Travel 7 Days A Week</li><li><svg><use href="#tick"/></svg>Many Destinations</li><li><svg><use href="#tick"/></svg>Good For Two Adults</li><li><svg><use href="#tick"/></svg>Pay Just The Taxes</li><li><svg><use href="#tick"/></svg>Flexible Dates Allowed</li><li><svg><use href="#tick"/></svg>Fully Transferable</li><li><svg><use href="#tick"/></svg>No Sales Pitch</li><li><svg><use href="#tick"/></svg>24 Months To Travel</li></ul>
  <h2 class="banner banner--teal banner--features">FEATURES</h2>
  <h2 class="banner banner--orange banner--how">HOW CAN WE DO THIS?</h2>
  <p class="copy copy--how">We contract with leading hotel chains to help fill their empty rooms. Hotels gain new guests for dining, spa and future stays, while you enjoy a great getaway at a reduced rate, again and again.</p>
  <blockquote class="testimonial">"We won this trip at a raffle and used it for our honeymoon. The hotel was amazing. Thank you!"<cite>Leo M. Atlanta, Georgia</cite></blockquote>
  <h2 class="banner banner--orange banner--say">WHAT OTHERS SAY</h2>
  <div class="cutline"></div><div class="divider"></div>
  <div class="cert"><p class="cert__label">Certificate ID</p><p class="cert__value">107083-11266</p><p class="cert__label">Expires</p><p class="cert__value">11/11/2020</p></div>
  <div class="redeem"><p class="redeem__title">VIEW ALL THE DETAILS OF THIS SPECIAL OFFER<br>AND REDEEM ONLINE AT</p><p class="redeem__url">WWW.GETAWAYREWARDSHUB.COM</p><p class="redeem__note">*Terms and Conditions apply see website for details</p></div>
</article>

<article class="flyer flyer--thumb thumb-6">
  <div class="hero" role="img" aria-label="Photo of a grand hotel lobby with chandeliers" style="background:linear-gradient(180deg,#6a4a30,#b08858 50%,#3a4a6a)"></div>
  <div class="sponsor"><p class="sponsor__label">Compliments Of</p><p class="sponsor__brand"><i></i>Northwind Rewards</p><p class="sponsor__name">Dana Ellis</p><p class="sponsor__phone">555-014-2290</p></div>
  <div class="headline"><h1 class="headline__main">ENJOY</h1><p class="headline__tag"><small>3 NIGHT</small><span>HOTEL STAY</span></p></div>
  <p class="subtitle">of 3+ Star Hotel Accommodations<br>In The City Of Your Choice Of<br>Over 50 of The Most Popular<br>Destinations Available!</p>
  <div class="photo photo--beach" role="img" aria-label="Photo of a hotel concierge" style="background:linear-gradient(160deg,#d8d0c4,#5a4a3a)"></div>
  <div class="photo photo--lounger" role="img" aria-label="Photo of a resort pool and palms" style="background:linear-gradient(160deg,#6ac0e8,#4a8a4a)"></div>
  <div class="photo photo--pool" role="img" aria-label="Photo of a bright hotel room doorway" style="background:linear-gradient(160deg,#f4eee6,#b8a890)"></div>
  <h2 class="banner banner--orange banner--exclusive">EXCLUSIVELY FOR:</h2>
  <p class="copy copy--exclusive">There is no doubt that everyone wishes they could take a much needed vacation. Enjoy three nights of hotel accommodations in the city of your choice, now you can enjoy a well earned break.</p>
  <ul class="features"><li><svg><use href="#tick"/></svg>Travel 7 Days A Week</li><li><svg><use href="#tick"/></svg>Over 50 Cities</li><li><svg><use href="#tick"/></svg>Good For Two Adults</li><li><svg><use href="#tick"/></svg>Pay Just The Taxes</li><li><svg><use href="#tick"/></svg>Flexible Dates Allowed</li><li><svg><use href="#tick"/></svg>Fully Transferable</li><li><svg><use href="#tick"/></svg>No Sales Pitch</li><li><svg><use href="#tick"/></svg>24 Months To Travel</li></ul>
  <h2 class="banner banner--teal banner--features">FEATURES</h2>
  <h2 class="banner banner--orange banner--how">HOW CAN WE DO THIS?</h2>
  <p class="copy copy--how">We contract with leading hotel chains to fill their empty rooms. Hotels earn from restaurants, room service and future bookings, while you enjoy a city break for just the taxes and fees.</p>
  <blockquote class="testimonial">"Being able to stay right on the strip was a treat. We loved the hotel and the whole trip. Thank you!"<cite>Leo M. San Diego, CA</cite></blockquote>
  <h2 class="banner banner--orange banner--say">WHAT OTHERS SAY</h2>
  <div class="cutline"></div><div class="divider"></div>
  <div class="cert"><p class="cert__label">Certificate ID</p><p class="cert__value">107083-11266</p><p class="cert__label">Expires</p><p class="cert__value">11/11/2020</p></div>
  <div class="redeem"><p class="redeem__title">VIEW ALL THE DETAILS OF THIS SPECIAL OFFER<br>AND REDEEM ONLINE AT</p><p class="redeem__url">WWW.GETAWAYREWARDSHUB.COM</p><p class="redeem__note">*Terms and Conditions apply see website for details</p></div>
</article>

</body>
</html>
```